Company Website Re-design for Software development consultancy

We would like our company website to be redesigned using our existing marketing collateral and website content as a guide

current site : www.brackenloft.com.au

For the different pages types and content please base on the following site : https://www.quorvanta.net/

We want a coded site - but will replace the content ourselves within the sections you provide to customise to our needs.

Target Market(s)

Medium to Large corporates needing software design and development services

Industry/Entity Type

Information Technology

Coding

Coded - Design and coding required

Number of Pages Required

5+ page

Font styles to use
Sans Serif

Colors
ec1f27
ffffff
000000

Requirements
Must have
• Align to colour scheme of existing collateral
• Include pages for the key areas of our busines - see : https://www.quorvanta.net/
Nice to have
• image rotators - make the site interesting to the business visitor

```html
<!DOCTYPE html>
<html lang="en">
<head>
<meta charset="utf-8">
<title>About Us – Bracken Loft</title>
<link href="https://fonts.googleapis.com/css2?family=Poppins:wght@400;500;600;700&family=Open+Sans:wght@400&display=swap" rel="stylesheet">
<style>
  :root {
    --brand-red: #ec1f27;
    --brand-red-dark: #8c0a10;
    --white: #ffffff;
    --black: #000000;
    --ink: #111111;
    --body-text: #555555;
    --band-grey: #ebebeb;
    --hero-tone-a: #4a3f3a;
    --hero-tone-b: #2d2826;
  }
  * { margin: 0; padding: 0; box-sizing: border-box; }
  html, body { width: 937px; height: 1200px; overflow: hidden; background: var(--white); }
  .page { position: relative; width: 937px; height: 1200px; overflow: hidden; font-family: "Poppins", sans-serif; color: var(--ink); }

  /* Hero */
  .hero { position: absolute; left: 0; top: 0; width: 937px; height: 342px; }
  .hero-photo { position: absolute; inset: 0; background: linear-gradient(120deg, var(--hero-tone-a) 0%, #5e524a 45%, var(--hero-tone-b) 100%); }
  .site-header { position: absolute; left: 142px; top: 24px; width: 660px; height: 30px; display: flex; align-items: center; }
  .brand-name { font-family: "Poppins", sans-serif; font-weight: 700; font-size: 23px; color: var(--white); letter-spacing: 0.5px; width: 234px; }
  .main-nav { display: flex; gap: 26px; }
  .main-nav a { color: var(--white); text-decoration: none; font-size: 11.5px; font-weight: 500; letter-spacing: 0.2px; }
  .hero-ring { position: absolute; left: 430px; top: 121px; width: 62px; height: 62px; border: 4px solid var(--brand-red); border-radius: 50%; }
  .hero-title { position: absolute; left: 0; width: 937px; top: 186px; text-align: center; color: var(--white); font-size: 40px; font-weight: 600; }

  /* About */
  .about-heading { position: absolute; left: 139px; top: 412px; font-size: 22px; font-weight: 600; color: var(--black); }
  .about-copy { position: absolute; left: 141px; top: 459px; width: 320px; font-family: "Open Sans", sans-serif; font-size: 11.6px; line-height: 20px; color: var(--body-text); }
  .about-visual { position: absolute; left: 504px; top: 416px; width: 316px; height: 220px; background: radial-gradient(circle at 50% 50%, #dbeaf5 0%, #f3f3f3 60%, #ffffff 100%); border-radius: 6px; }

  /* Team */
  .team-band { position: absolute; left: 0; top: 690px; width: 937px; height: 460px; }
  .team-title { position: absolute; left: 0; width: 937px; top: 761px; text-align: center; color: var(--brand-red); font-size: 21px; font-weight: 700; }
  .member { position: absolute; top: 819px; width: 200px; text-align: center; }
  .member-photo { width: 154px; height: 154px; border-radius: 50%; margin: 0 auto; background: radial-gradient(circle at 50% 40%, #c9c4bd 0%, #8f8d88 70%, #5b5d63 100%); border: 1px solid #cfcfcf; }
  .member-name { margin-top: 8px; font-size: 15px; font-weight: 600; color: var(--ink); line-height: 18px; }
  .member-role { font-size: 10px; color: var(--ink); line-height: 14px; }
  .member-bio { font-size: 11px; color: var(--ink); line-height: 13px; margin-top: 2px; }

  /* Footer */
  .site-footer { position: absolute; left: 0; top: 1155px; width: 937px; height: 24px; }
  .copyright { position: absolute; left: 297px; top: 3px; font-family: "Open Sans", sans-serif; font-size: 12px; color: #444444; }
  .social-links { position: absolute; left: 670px; top: 2px; display: flex; gap: 20px; }
  .social-dot { width: 16px; height: 16px; border-radius: 50%; background: #444444; }
</style>
</head>
<body>
<div class="page">

  <section class="hero">
    <div class="hero-photo" role="img" aria-label="Photo of colleagues working together at a desk, dark warm overlay"></div>
    <header class="site-header">
      <div class="brand-name">BRACKEN LOFT</div>
      <nav class="main-nav">
        <a href="#">ABOUT US</a>
        <a href="#">PRODUCTS AND SERVICES</a>
        <a href="#">BLOG ARTICLE</a>
        <a href="#">CONTACT</a>
      </nav>
    </header>
    <div class="hero-ring"></div>
    <h1 class="hero-title">ABOUT US</h1>
  </section>

  <section class="about">
    <h2 class="about-heading">ABOUT BRACKEN LOFT</h2>
    <p class="about-copy">After spending more than twenty years each in the industry, including seven years in New York building electronic trading systems for Harlow Whitcombe – the founders realised that there was a distinct lack in the market of people focusing on how software is developed – not just solving the business problem, but automating the development itself to increase both productivity and quality.</p>
    <div class="about-visual" role="img" aria-label="Illustration of a laptop surrounded by software development icons"></div>
  </section>

  <svg class="team-band" viewBox="0 0 937 460" width="937" height="460" aria-hidden="true">
    <polygon points="0,4 937,34 937,450 0,414" fill="#ebebeb"/>
    <polygon points="716,35 937,14 937,46" fill="#ec1f27"/>
    <polygon points="716,35 937,14 937,24" fill="#8c0a10"/>
    <polygon points="0,414 212,423 0,444" fill="#ec1f27"/>
    <polygon points="0,430 212,423 0,444" fill="#8c0a10"/>
  </svg>

  <h2 class="team-title">OUR TEAM</h2>

  <div class="member" style="left:133px;">
    <div class="member-photo" role="img" aria-label="Portrait photo of Callum Redfern"></div>
    <div class="member-name">Callum Redfern</div>
    <div class="member-role">PARTNER</div>
    <div class="member-bio">Callum's one of the best developers<br>on the planet</div>
  </div>
  <div class="member" style="left:371px;">
    <div class="member-photo" role="img" aria-label="Portrait photo of Owen Thackery"></div>
    <div class="member-name">Owen Thackery</div>
    <div class="member-role">PARTNER</div>
    <div class="member-bio">Owen's been running software<br>projects for 20 years</div>
  </div>
  <div class="member" style="left:611px;">
    <div class="member-photo" role="img" aria-label="Portrait photo of Lewis Brandt"></div>
    <div class="member-name">Lewis Brandt</div>
    <div class="member-role">PARTNER</div>
    <div class="member-bio">Lewis codes for fun as much as<br>he does for work</div>
  </div>

  <footer class="site-footer">
    <p class="copyright">© 2018 Company Name&nbsp; All right reserved&nbsp; Term of Use</p>
    <div class="social-links">
      <span class="social-dot" aria-label="Social link"></span>
      <span class="social-dot" aria-label="Social link"></span>
      <span class="social-dot" aria-label="Social link"></span>
      <span class="social-dot" aria-label="Social link"></span>
    </div>
  </footer>

</div>
</body>
</html>
```